Managed Service Provider need new business cards

We are a small Maanged Service Provider of IT Services and need a new fresh design for our business cards. We want something impossible, fun and professional :)
Our services has a large range, but we are always fun and make sure our customers both get their issue sorted and also feel like they are "catching up with an old friend".
All our cards in the past has always been all black, with red and we need something fresher.
The back of card, we would like just a small list of what we do i think, but if someone has a better idea, please do something cool with the back of the card:
Managed IT Services
Productivity Solutions
Data Backup and Recovery
IT System Maintenance
Managed IT Security
More details can be found on our website tqnetworks.com.au
Industry/Entity Type
It Company
Contact Information for Business Card
Name: Dwayne Falstrup
Title: Director
Phone: 03 6193 4827
Mobile: 0412 587 239
Email: dwayne@tqnetworks.com.au
Web: www.tqnetworks.com.au

```html
<!DOCTYPE html>
<html lang="en">
<head>
<meta charset="UTF-8">
<title>TQ Networks – Business Cards</title>
<link rel="stylesheet" href="https://fonts.googleapis.com/css2?family=Lato:wght@400;700;900&family=Montserrat:wght@400;500&display=swap">
<style>
  :root {
    --backdrop: #3a3633;
    --card: #1f1f1f;
    --card-light: #2a2a2a;
    --red: #e3212b;
    --white: #ffffff;
    --muted: #d9d9d9;
  }
  * { box-sizing: border-box; margin: 0; padding: 0; }
  html, body {
    width: 1200px;
    height: 900px;
    overflow: hidden;
    background: var(--backdrop);
    font-family: "Lato", Arial, sans-serif;
  }
  .sheet {
    position: relative;
    width: 1200px;
    height: 900px;
  }
  .card {
    position: absolute;
    width: 700px;
    height: 400px;
    border-radius: 26px;
    background: linear-gradient(135deg, var(--card-light) 0%, var(--card) 55%, #1a1a1a 100%);
    box-shadow: 0 14px 30px rgba(0,0,0,0.45);
    overflow: hidden;
  }
  .card--back { left: 110px; top: 40px; }
  .card--front { left: 390px; top: 470px; }

  .brand {
    display: flex;
    align-items: center;
    gap: 14px;
    color: var(--red);
    font-family: "Lato", Arial, sans-serif;
    font-weight: 900;
    text-transform: uppercase;
    letter-spacing: 1px;
    white-space: nowrap;
  }
  .brand__dot {
    display: inline-block;
    border-radius: 50%;
    background: var(--red);
  }

  /* Back: services */
  .card--back .brand {
    position: absolute;
    left: 0;
    right: 0;
    top: 120px;
    justify-content: center;
    font-size: 64px;
  }
  .card--back .brand__dot { width: 40px; height: 40px; }
  .services {
    position: absolute;
    left: 40px;
    right: 40px;
    top: 262px;
    text-align: center;
    font-family: "Montserrat", Arial, sans-serif;
    font-weight: 500;
    font-size: 17px;
    line-height: 30px;
    color: var(--white);
  }
  .services__bullet { color: var(--red); margin: 0 6px; }

  /* Front: contact */
  .card--front .brand {
    position: absolute;
    right: 50px;
    top: 54px;
    font-size: 40px;
  }
  .card--front .brand__dot { width: 26px; height: 26px; }
  .identity {
    position: absolute;
    left: 70px;
    top: 178px;
  }
  .identity__bar {
    position: absolute;
    left: -70px;
    top: 42px;
    width: 16px;
    height: 62px;
    background: var(--red);
  }
  .identity__name {
    font-weight: 700;
    font-size: 38px;
    color: var(--red);
    line-height: 44px;
  }
  .identity__title {
    font-size: 24px;
    color: var(--white);
    line-height: 32px;
  }
  .contacts {
    position: absolute;
    left: 70px;
    top: 268px;
    list-style: none;
    font-size: 22px;
    line-height: 29px;
    color: var(--white);
  }
  .contacts__item { display: flex; align-items: center; gap: 12px; }
  .contacts__icon { width: 18px; height: 18px; flex: none; }
  .contacts__accent { color: var(--red); }
</style>
</head>
<body>
<main class="sheet">

  <section class="card card--back" aria-label="Card back: services">
    <div class="brand"><span class="brand__dot"></span>TQ Networks</div>
    <p class="services">
      Managed IT Services <span class="services__bullet">•</span> Productivity Solutions <span class="services__bullet">•</span> Data Backup and Recovery<br>
      <span class="services__bullet">•</span> IT System Maintenance <span class="services__bullet">•</span> Managed IT Security
    </p>
  </section>

  <section class="card card--front" aria-label="Card front: contact details">
    <div class="brand"><span class="brand__dot"></span>TQ Networks</div>
    <div class="identity">
      <span class="identity__bar"></span>
      <h1 class="identity__name">Dwayne Falstrup</h1>
      <p class="identity__title">Director</p>
    </div>
    <ul class="contacts">
      <li class="contacts__item">
        <svg class="contacts__icon" viewBox="0 0 24 24" aria-hidden="true"><path fill="#e3212b" d="M6.6 10.8a15 15 0 0 0 6.6 6.6l2.2-2.2a1 1 0 0 1 1-.25 11.4 11.4 0 0 0 3.6.57 1 1 0 0 1 1 1V20a1 1 0 0 1-1 1A17 17 0 0 1 3 4a1 1 0 0 1 1-1h3.5a1 1 0 0 1 1 1c0 1.25.2 2.45.57 3.57a1 1 0 0 1-.25 1z"/></svg>
        03 6193 4827
      </li>
      <li class="contacts__item">
        <svg class="contacts__icon" viewBox="0 0 24 24" aria-hidden="true"><rect x="6" y="2" width="12" height="20" rx="2" fill="none" stroke="#e3212b" stroke-width="2"/><circle cx="12" cy="18" r="1.2" fill="#e3212b"/></svg>
        0412 587 239
      </li>
      <li class="contacts__item">
        <svg class="contacts__icon" viewBox="0 0 24 24" aria-hidden="true"><rect x="2" y="5" width="20" height="14" rx="1" fill="#e3212b"/><path d="M2 6l10 7 10-7" fill="none" stroke="#1f1f1f" stroke-width="1.6"/></svg>
        dwayne@tqnetworks.com.au
      </li>
      <li class="contacts__item">
        <svg class="contacts__icon" viewBox="0 0 24 24" aria-hidden="true"><circle cx="12" cy="12" r="10" fill="#e3212b"/><path d="M2 12h20M12 2c3 3 3 17 0 20M12 2c-3 3-3 17 0 20" fill="none" stroke="#1f1f1f" stroke-width="1.4"/></svg>
        <span>www.<span class="contacts__accent">tqnetworks</span>.com.au</span>
      </li>
    </ul>
  </section>

</main>
</body>
</html>
```